Scented Candle Company Sticker Design for Packaging

We need a Sticker design for our various scented candle packages. Our handmade candles incorperate hand crafted Chiyogami Paper imported from Japan, which is wrapped around the jar. Each of the scents have different papers assigned to them and although we would like a general design in which the text can be changed according to each scent we would also like if the beautiful Japanese paper designs could be subtly incorporated in the design.

We want the the text of the sticker and logo of our company to be printed in gold foil once printed and our featured logo image is of a Dogwood tree. We think that perhaps the inclusion of dogwood blossom/s might look nice in the design but is not a must have!

We are fond of the delicate and classic print designs and etching designs. We would also like the design to be in a portrait rectangle that is closer in the shape of a square/ or not too long of a rectangle, and, would like to have a boarder on the edge of the sticker (this could incorporate the blossom if you wish, I have attached an image for reference/ inspiration) but we are after something much more simplistic and draws less attention to the eye and connected in the boarder.

Our brand is elegant and classic and we would like to be in keeping with our style. We have attached some images of the candles and our logo for inspiration, we do not want the stickers for the candle themselves but rather to place on the packaging.

Ive left some information for one of the candle scents for this design but once again I would like to reiterate that the design should allow for interchangeable titles for the other fragrances.

Japanese Cherry Blossom(in smaller writing).
Japanese cherry blossom, Orange blossom, cinnamon.

Our candles are hand made in Australia and a made from 100% soy wax and we would like to to be presented on the label.

I would like to mention again that we are looking for an elegant and classic design. We are looking for a simplistic design/layout that also focuses on the fine details. It should be striking but also not overbearing with an air of sophistication with minimal to no use of colours in encouraged.

I have also attached a font that is matched to the "candle co." underneath the tree in the logo.
Updates

I only just posted the design request, but first created the brief on the 2nd. I would like more time for the designers to both see my review and have an adequate amount of time to work on the project.

Target Market(s)

Up Market Shoppers.

Font styles to use
Script
Other font styles liked:
• Acorn

Colors
fbfbfb

Requirements
Must have
• Logo on the sticker.
Nice to have
• Nice to have a dogwood blossom incorporated into the boarder but must be simplistic as it doesn't want to be the main focus of the sticker
Should not have
• Photographs in the sticker design. Must be graphic design. No to little colour.

```html
<!DOCTYPE html>
<html lang="en">
<head>
<meta charset="utf-8">
<title>Willowmere Candle Co. – Packaging Sticker</title>
<link rel="stylesheet" href="https://fonts.googleapis.com/css2?family=Josefin+Sans:wght@400&display=swap">
<style>
  :root {
    --backdrop: #000000;
    --paper: #ffffff;
    --ink: #0a0a0a;
    --ornament-tone: #d9d9d9;
  }
  * { margin: 0; padding: 0; box-sizing: border-box; }
  html, body {
    width: 1200px;
    height: 1200px;
    overflow: hidden;
    background: var(--backdrop);
  }
  .canvas {
    position: relative;
    width: 1200px;
    height: 1200px;
    background: var(--backdrop);
    font-family: "Josefin Sans", sans-serif;
    color: var(--ink);
  }
  .sticker {
    position: absolute;
    left: 172px;
    top: 172px;
    width: 856px;
    height: 855px;
    background: var(--paper);
  }
  .sticker__frame {
    position: absolute;
    left: 203px;
    top: 219px;
    width: 799px;
    height: 773px;
    border: 3px solid var(--ink);
  }
  .corner-ornament {
    position: absolute;
    width: 124px;
    height: 130px;
    background: var(--ornament-tone);
  }
  .corner-ornament--tl { left: 201px; top: 210px; }
  .corner-ornament--tr { left: 877px; top: 210px; }
  .corner-ornament--bl { left: 201px; top: 872px; }
  .corner-ornament--br { left: 877px; top: 872px; }

  .brand-mark {
    position: absolute;
    left: 548px;
    top: 368px;
    width: 104px;
    height: 104px;
    border-radius: 50%;
    background: var(--ink);
  }
  .brand-name {
    position: absolute;
    left: 0;
    width: 1200px;
    text-align: center;
    font-weight: 400;
    white-space: nowrap;
  }
  .brand-name--primary {
    top: 536px;
    font-size: 72px;
    letter-spacing: 10px;
    line-height: 80px;
  }
  .brand-name--secondary {
    top: 624px;
    font-size: 29px;
    letter-spacing: 3px;
    line-height: 32px;
  }
  .scent-title {
    position: absolute;
    left: 333px;
    top: 700px;
    width: 532px;
    height: 64px;
    border: 3px solid var(--ink);
    display: flex;
    align-items: center;
    justify-content: center;
    font-size: 26px;
    letter-spacing: 2px;
    padding-top: 4px;
  }
  .product-facts {
    position: absolute;
    left: 0;
    top: 810px;
    width: 1200px;
    text-align: center;
    font-size: 21px;
    line-height: 32px;
    letter-spacing: 0.5px;
  }
</style>
</head>
<body>
  <main class="canvas">
    <section class="sticker" aria-label="Candle packaging sticker"></section>
    <div class="sticker__frame"></div>

    <div class="corner-ornament corner-ornament--tl" role="img" aria-label="Blossom cluster corner ornament"></div>
    <div class="corner-ornament corner-ornament--tr" role="img" aria-label="Blossom cluster corner ornament"></div>
    <div class="corner-ornament corner-ornament--bl" role="img" aria-label="Blossom cluster corner ornament"></div>
    <div class="corner-ornament corner-ornament--br" role="img" aria-label="Blossom cluster corner ornament"></div>

    <div class="brand-mark" aria-hidden="true"></div>
    <h1 class="brand-name brand-name--primary">WILLOWMERE</h1>
    <p class="brand-name brand-name--secondary">CANDLE CO.</p>

    <h2 class="scent-title">JAPANESE CHERRY BLOSSOM</h2>

    <p class="product-facts">100% SOY WAX<br>MADE IN AUSTRALIA</p>
  </main>
</body>
</html>
```